Business card for a shipping supplies business

Needing a business card design. Please see the logo. The logo with the white font should be used if there is a dark background.

We are looking for the following info on the card. Please see the sample info. We will need the info to be changed with a few different employee names and info but all will use the same template.

Business Name: The Crate Heron
Employee Name : Marcus Delaney
Position: Account Manager
Address: 4827 W. Ridge 418 S.
Fort Worth, TX 73948
email: Marcus@thecrateheron.example
telephone: 855-619-2740 x 207
website: www.getparcelkits.example

Target Market(s)

Businesses who ship products for online sales

Industry/Entity Type

Cardboard

Contact Information for Business Card

Name, title, address, website, logo, telephone number

Font styles to use
Sans Serif

Colors
EE7325
F08F49
F5BC92
FAE3D3
FDF4ED

Requirements
Must have
• Logo on back of card. Clean look, just logo, website address

```html
<!DOCTYPE html>
<html lang="en">
<head>
<meta charset="utf-8">
<title>The Crate Heron — Business Card</title>
<link rel="stylesheet" href="https://fonts.googleapis.com/css2?family=Montserrat:wght@400;500;600;700;800&display=swap">
<style>
  :root {
    --orange: #EE7325;
    --orange-soft: #F08F49;
    --peach: #F5BC92;
    --cream: #FAE3D3;
    --paper: #FDF4ED;
    --card-black: #1c1c1c;
    --card-brown: #221d1a;
    --ink-white: #ffffff;
    --ink-grey: #d9d9d9;
    --stage: #dcdcdc;
  }
  * { box-sizing: border-box; margin: 0; padding: 0; }
  html, body {
    width: 1200px; height: 800px; overflow: hidden;
    background: var(--stage);
    font-family: "Montserrat", sans-serif;
  }
  .canvas {
    width: 1200px; height: 800px;
    display: flex; align-items: center; justify-content: center; gap: 48px;
  }
  .card {
    position: relative;
    width: 540px; height: 309px;
    border-radius: 22px;
    overflow: hidden;
    box-shadow: 0 18px 40px rgba(0,0,0,0.25);
  }
  /* Front side */
  .card--front { background: var(--card-black); }
  .front-divider {
    position: absolute; left: 0; top: 0; width: 100%; height: 100%;
  }
  .brand-block {
    position: absolute; left: 46px; top: 0; bottom: 0; width: 230px;
    display: flex; flex-direction: column; align-items: center; justify-content: center; gap: 16px;
  }
  .brand-mark-area {
    width: 120px; height: 96px; border-radius: 50%;
    background: radial-gradient(circle at 45% 45%, #b9805a 0%, #a4582a 55%, #3a2418 100%);
  }
  .brand-name {
    display: flex; align-items: center; gap: 8px;
    font-weight: 800; font-size: 20px; letter-spacing: 1px;
    color: var(--ink-white); text-transform: uppercase; white-space: nowrap;
  }
  .brand-dot { width: 10px; height: 10px; border-radius: 50%; background: var(--orange); }
  .contact-block {
    position: absolute; left: 296px; top: 62px; right: 20px;
    color: var(--ink-white);
  }
  .person-name { font-weight: 700; font-size: 19px; letter-spacing: 0.5px; text-transform: uppercase; }
  .person-title { font-weight: 500; font-size: 12.5px; color: var(--orange); margin-top: 2px; }
  .address { font-size: 11.5px; line-height: 1.45; margin-top: 16px; color: var(--ink-grey); }
  .contact-list { list-style: none; margin-top: 14px; }
  .contact-list li {
    display: flex; align-items: center; gap: 8px;
    font-size: 10.5px; line-height: 1.8; color: var(--ink-grey); white-space: nowrap;
  }
  .contact-icon { width: 11px; height: 11px; flex: none; }
  /* Back side */
  .card--back { background: var(--card-brown); }
  .back-decoration {
    position: absolute; inset: 0;
    background:
      radial-gradient(ellipse at 18% 80%, rgba(80,50,35,0.35) 0%, transparent 55%),
      linear-gradient(120deg, #2a2420 0%, #211c19 50%, #1b1816 100%);
  }
  .back-content {
    position: absolute; inset: 0;
    display: flex; flex-direction: column; align-items: center; justify-content: center;
  }
  .back-content .brand-mark-area { width: 150px; height: 118px; }
  .back-content .brand-name { font-size: 28px; margin-top: 18px; }
  .back-content .brand-dot { width: 13px; height: 13px; }
  .back-website {
    margin-top: 30px; font-size: 13px; letter-spacing: 1.5px; color: var(--ink-white);
  }
</style>
</head>
<body>
<main class="canvas">
  <section class="card card--front" aria-label="Card front">
    <svg class="front-divider" viewBox="0 0 540 309" aria-hidden="true">
      <line x1="250" y1="150" x2="330" y2="205" stroke="#3a3a3a" stroke-width="1"/>
    </svg>
    <div class="brand-block">
      <div class="brand-mark-area" role="img" aria-label="Brand illustration area: orange fox holding a cardboard box"></div>
      <div class="brand-name"><span class="brand-dot"></span>The Crate Heron</div>
    </div>
    <div class="contact-block">
      <h1 class="person-name">Marcus Delaney</h1>
      <p class="person-title">Account Manager</p>
      <p class="address">4827 W. Ridge 418 S.<br>Fort Worth, TX 73948</p>
      <ul class="contact-list">
        <li>
          <svg class="contact-icon" viewBox="0 0 12 12"><path d="M3 1 L5 3.5 L4 5 Q5 7 7 8 L8.5 7 L11 9 L10 11 Q4 11 1 3 Z" fill="var(--orange)"/></svg>
          855-619-2740 x 207
        </li>
        <li>
          <svg class="contact-icon" viewBox="0 0 12 12"><rect x="1" y="2.5" width="10" height="7" rx="1" fill="var(--orange)"/><path d="M1.5 3 L6 6.5 L10.5 3" stroke="var(--card-black)" stroke-width="1" fill="none"/></svg>
          Marcus@thecrateheron.example
        </li>
        <li>
          <svg class="contact-icon" viewBox="0 0 12 12"><circle cx="6" cy="6" r="5" fill="var(--orange)"/><path d="M1 6 H11 M6 1 Q3 6 6 11 M6 1 Q9 6 6 11" stroke="var(--card-black)" stroke-width="0.8" fill="none"/></svg>
          getparcelkits.example
        </li>
      </ul>
    </div>
  </section>

  <section class="card card--back" aria-label="Card back">
    <div class="back-decoration" role="img" aria-label="Faint large brand illustration in dark tones"></div>
    <div class="back-content">
      <div class="brand-mark-area" role="img" aria-label="Brand illustration area: orange fox holding a cardboard box"></div>
      <div class="brand-name"><span class="brand-dot"></span>The Crate Heron</div>
      <p class="back-website">www.getparcelkits.example</p>
    </div>
  </section>
</main>
</body>
</html>
```